Letterhead for SaaS

Design a letterhead that aligns with our new business card, using our logo and color scheme and text defined in the Branding Guide to ensure consistency. Consider incorporating a subtle watermark for added elegance. The layout should reflect the card's style, creating a cohesive look across our stationery.

```html
<!DOCTYPE html>
<html lang="en">
<head>
<meta charset="utf-8">
<title>Norvale Letterhead</title>
<link rel="stylesheet" href="https://fonts.googleapis.com/css2?family=Arimo:wght@400;700&display=swap">
<style>
  :root {
    --backdrop: #d9d9da;
    --paper: #ffffff;
    --ink: #1c1e24;
    --body-ink: #3a3c42;
    --muted: #8f9196;
    --rule: #b9babd;
    --navy: #1b2230;
    --accent: #1eb6ec;
    --watermark: #f1f2f4;
  }
  * { box-sizing: border-box; margin: 0; padding: 0; }
  html, body { width: 1200px; height: 1159px; overflow: hidden; }
  body {
    background: var(--backdrop);
    font-family: "Arimo", Arial, sans-serif;
    color: var(--ink);
    position: relative;
  }
  .letterhead {
    position: absolute;
    left: 204px; top: 20px;
    width: 792px; height: 1119px;
    background: var(--paper);
    box-shadow: 0 6px 24px rgba(0,0,0,.18);
    overflow: hidden;
  }
  .brand {
    position: absolute;
    top: 70px; left: 0; right: 0;
    display: flex; flex-direction: column; align-items: center; gap: 12px;
  }
  .brand-mark {
    width: 34px; height: 34px; border-radius: 50%;
    background: var(--navy);
  }
  .brand-name {
    font-weight: 700; font-size: 26px; letter-spacing: 2px; color: var(--ink);
  }
  .watermark-area {
    position: absolute;
    left: 250px; top: 290px; width: 330px; height: 470px;
    background: radial-gradient(ellipse at center, var(--watermark) 0%, rgba(241,242,244,0.6) 55%, rgba(255,255,255,0) 75%);
  }
  .letter-body {
    position: absolute;
    left: 92px; top: 330px; width: 590px;
    font-size: 13.5px; line-height: 1.42; color: var(--body-ink);
  }
  .greeting {
    font-size: 18px; font-weight: 700; color: var(--ink);
    margin-bottom: 22px;
  }
  .letter-body p { margin-bottom: 22px; }
  .closing {
    margin-top: 36px; font-size: 12px; font-weight: 700; color: var(--ink);
  }
  .signature-area {
    margin-top: 22px; width: 170px; height: 46px;
    background: linear-gradient(90deg, #eeeef0, #f7f7f8);
    border-radius: 4px;
  }
  .contact-rule {
    position: absolute;
    left: 300px; right: 60px; bottom: 104px;
    height: 2px; background: var(--rule);
  }
  .contact-list {
    position: absolute;
    right: 60px; bottom: 72px;
    display: flex; gap: 22px; align-items: center;
    font-size: 15px; color: var(--body-ink);
    list-style: none;
  }
  .contact-list li { display: flex; align-items: center; gap: 7px; }
  .contact-list svg { width: 14px; height: 14px; fill: var(--accent); }
  .footer-band {
    position: absolute; left: 0; bottom: 0; width: 100%; height: 30px;
  }
</style>
</head>
<body>
  <article class="letterhead">
    <header class="brand">
      <span class="brand-mark"></span>
      <span class="brand-name">NORVALE</span>
    </header>

    <div class="watermark-area" role="img" aria-label="Faint brand watermark in the page centre"></div>

    <section class="letter-body">
      <h1 class="greeting">Dear Mr. Harlow,</h1>
      <p>Lorem ipsum dolor sit amet, consectetuer adipiscing elit, sed diam nonmmy nibh euismod tincidunt ut laor eet dolore magna aliquam erat volutpat. Ut wisi enim ad minim veniam, quis nostrud exerci tationmcorper suscipit lobortis nisl ut aliquip ex ea commodo consequat. Duis autem vel eum iriure dolor in hendrerit in vulputate velit esse molestie consequat, vel illum dolore eu feugiat</p>
      <p>Rorem ipsum dolor sit amet, consectetuer adipiscing elit, sed diam nonmmy nibh euismod tincidunt ut laor eet dolore magna aliquam erat volutpat. Ut wisi enim ad minim veniam, quis nostrud exerci tationmcorper suscipit lobortis nisl ut aliquip ex ea commodo consequat. Duis autem vel eum iriure dolor in hendrerit in vulputate velit esse molest</p>
      <p>Dorem ipsum dolor sit amet, consectetuer adipiscing elit, sed diam nonmmy nibh euismod tincidunt ut laor eet dolore magna aliquam erat volutpat. Ut wisi enim ad minim veniam, quis nostrud exerci tationmcorper suscipit lobortis nisl ut aliquip ex ea commodo consequat. Duis autem vel eum iriure dolor in hendrerit in suscipit lobortis nisl ut aliquip ex ea commodo consequat. Duis autem vel eum iriure dolor in hendrerit in vulputate velit esse molestie consequat, vel illum</p>
      <p>Sorem ipsum dolor sit amet, consectetuer adipiscing elit, sed diam nonmmy nibh euismod tincidunt ut laor eet dolore magna aliquam erat volutpat. Ut wisi enim ad minim veniam, quis nostrud exerci tationmcorper suscipit lobortis nisl ut aliquip ex ea commodo consequat. Duis autem vel eum iriure dolor in</p>
      <p class="closing">Sincerely,</p>
      <div class="signature-area" role="img" aria-label="Handwritten signature of the sender"></div>
    </section>

    <div class="contact-rule"></div>
    <ul class="contact-list">
      <li><svg viewBox="0 0 16 16"><path d="M3 1h3l1.5 4-2 1.3a9 9 0 0 0 4.2 4.2L11 8.5l4 1.5v3a2 2 0 0 1-2 2A12 12 0 0 1 1 3a2 2 0 0 1 2-2z"/></svg>044-555 018 273</li>
      <li><svg viewBox="0 0 16 16"><path d="M1 4h14v9H1z M1 4l7 5 7-5" stroke="#fff" stroke-width="1"/></svg>hello@norvale.io</li>
      <li><svg viewBox="0 0 16 16"><circle cx="8" cy="8" r="7"/><path d="M1 8h14M8 1c3 3 3 11 0 14M8 1c-3 3-3 11 0 14" stroke="#fff" stroke-width="1" fill="none"/></svg>www.norvale.io</li>
    </ul>

    <svg class="footer-band" viewBox="0 0 792 30" preserveAspectRatio="none" aria-hidden="true">
      <polygon points="0,22 700,22 690,30 0,30" fill="var(--navy)"/>
      <polygon points="712,0 792,0 792,30 700,30" fill="var(--accent)"/>
    </svg>
  </article>
</body>
</html>
```